Willowmere Veterinary Practice including Nest2Nurse

We require a double-sided full colour tri-fold Brochure for Print.
Colour theme to in line with logo below

Written CONTENT below
Orphans
We can provide care and a new mother for orphan foals of any age, breed or size, from thoroughbreds and draft breeds to tiny ponies and even donkeys.
We have successfully fostered orphans from a few hours of age through to eight weeks, regardless of how long or if at all they were with their birth mother, and of previous fostering attempts.
We have the knowledge and experience to provide optimum nutrition and care to orphans during the brief period that they don’t have a mum, until their new foster mother is ready to take them.
Additionally we are a veterinary practice, and can provide diagnostics and therapeutics for compromised orphan foals such as plasma administration and health checks.

Mares
Nest2Nurse mares have been selected for mothering ability and temperament, and have all carried and raised at least one foal of their own. Many have already been successful foster mothers in one or more of the last five breeding seasons.
The mares are not currently pregnant and are given a carefully designed course of hormones to induce lactation when required. The milk produced is not colostrum, but is completely normal and equivalent to that which they would have had if the foal was theirs by birth.
There is published scientific information (in addition to our own experience and that of the owners of previous graduates of our programme) that growth and development of foals raised by induced lactation is identical to that of foals raised by their birth mothers.

Fostering
During the few days when the mare’s udder is developing, mare and foal are kept next separately but in close proximity, allowing bonding to begin and reducing stress on the orphan.
The fostering is completed once the mare has enough milk to feed the foal, and our experienced handlers ensure that joining the two goes smoothly.
Once they are together the mare completely accepts the foal as her own, and the foal can suckle freely – at this stage we continue to offer supplementary feeds until they are not needed.
The mare and foal are then a normal unit and can return to the foal owner’s care until weaning – ensuring optimum nutrition and behaviour for the foal and excellent outcomes in performance, relationships with other horses, and interaction with humans.

Complete Safety
Mares recognise their birth foal by scent - a unique bond established during the first few minutes of the foal’s life - and only a small percentage of mares who have lost their own foal will readily accept a substitute.
When a mare who has lost her birth foal is offered an orphan, it is very normal and common for her to respond with aggression - to the danger of the foal and the human handler.
Nest2Nurse mares have no birth foal in the current season, and are happy to adopt any foal who is placed close to them during the hormone treatment period.
This makes for total foal and handler safety.

Excellent Success Rate
After seven years of perfecting the fostering method, Nest2Nurse can claim total success: we have now documented almost 50 fosterings over the last five breeding seasons. We have never been entrusted with an orphan foal that we have not been able to provide with a beautiful foster mum.

Career Mothers
Being dedicated career mothers with no other job in life, our mares are free to accompany their new foals home and stay with them as long as required. No foals are weaned and left without a mother in our programme, and our beautiful mares who would otherwise not be bred, are given a foal every year and a wonderful lifelong purpose.

Every single orphan’s human family has admired and appreciated our beautiful mares, with many offering to give them a home for life. Each season as the orphans are weaned, we welcome our mares home to Willowmere to prepare for the next foal in need – a job they totally love! – just as if they were in a natural breeding situation.

Willowmere Vet Practice including Nest2Nurse
218 Pellbrook Lane
Tarrick. Vic. 3872

Phone 0491583620 or 0438261597

```html
<!DOCTYPE html>
<html lang="en">
<head>
<meta charset="utf-8">
<title>Willowmere Tri-fold Brochure</title>
<link href="https://fonts.googleapis.com/css2?family=Open+Sans:wght@400;600;700&family=Oswald:wght@400;600;700&display=swap" rel="stylesheet">
<style>
  :root {
    --stage: #c9c9c9;
    --frame: #2b2d2c;
    --orange: #f26f21;
    --ink: #3a3f44;
    --sky: #cfe3f3;
    --mist: #eef3f5;
    --grass: #c9d7a6;
    --white: #ffffff;
  }
  * { box-sizing: border-box; margin: 0; padding: 0; }
  html, body { width: 893px; height: 1200px; overflow: hidden; }
  body {
    background: var(--stage);
    font-family: 'Open Sans', sans-serif;
    color: var(--ink);
    position: relative;
  }
  .spread {
    position: absolute;
    left: 61px;
    width: 771px;
    height: 566px;
    background: var(--frame);
    display: flex;
    padding: 12px;
    gap: 0;
    box-shadow: 0 6px 18px rgba(0,0,0,.25);
  }
  .spread--outside { top: 24px; }
  .spread--inside { top: 610px; }
  .panel {
    flex: 1;
    position: relative;
    overflow: hidden;
    background: linear-gradient(180deg, var(--sky) 0%, var(--mist) 55%, var(--grass) 100%);
    border-right: 1px solid rgba(0,0,0,.08);
  }
  .panel:first-child { border-radius: 16px 0 0 16px; }
  .panel:last-child { border-radius: 0 16px 16px 0; border-right: none; }
  .panel--cover { background: var(--frame); }
  .content { position: absolute; left: 14px; right: 14px; }
  .tag {
    display: inline-block;
    background: var(--orange);
    color: var(--white);
    font-family: 'Oswald', sans-serif;
    font-weight: 600;
    font-size: 12px;
    letter-spacing: .3px;
    padding: 1px 10px 2px;
    border-radius: 10px;
    margin: 0 0 5px;
  }
  .body-text p {
    font-size: 6.6px;
    line-height: 1.38;
    text-align: justify;
    margin-bottom: 5px;
  }
  .photo { position: absolute; }
  .brand-name {
    font-family: 'Open Sans', sans-serif;
    font-weight: 600;
    color: var(--orange);
    font-size: 15px;
    display: flex; align-items: center; gap: 6px;
    justify-content: center;
  }
  .brand-name .dot { width: 12px; height: 12px; border-radius: 50%; background: var(--orange); }
  .contact { text-align: center; font-size: 7px; line-height: 1.4; }
  .contact .sub { font-size: 6.5px; margin: 8px 0 18px; }
  .contact-item { margin-bottom: 15px; }
  .contact-item svg { display: block; margin: 0 auto 4px; }
  .cover-brand { position: absolute; top: 14px; left: 0; right: 0; }
  .headline {
    position: absolute; left: 16px; right: 16px; bottom: 110px;
    font-family: 'Oswald', sans-serif; color: var(--white); text-align: center;
  }
  .headline .l1 { font-size: 22px; font-weight: 600; line-height: 1.1; }
  .headline .l2 { font-size: 42px; font-weight: 700; color: var(--orange); line-height: 1; letter-spacing: 1px; }
  .headline .l3 { font-size: 17px; font-weight: 400; line-height: 1.2; }
</style>
</head>
<body>

<section class="spread spread--outside" aria-label="Brochure outside">
  <article class="panel panel--orphans">
    <div class="content" style="top:14px">
      <h2 class="tag">Orphans</h2>
      <div class="body-text">
        <p>We can provide care and a new mother for orphan foals of any age, breed or size, from thoroughbreds and draft breeds to tiny ponies and even donkeys.</p>
        <p>We have successfully fostered orphans from a few hours of age through to eight weeks, regardless of how long or if at all they were with their birth mother, and of previous fostering attempts.</p>
        <p>We have the knowledge and experience to provide optimum nutrition and care to orphans during the brief period that they don’t have a mum, until their new foster mother is ready to take them.</p>
        <p>Additionally we are a veterinary practice, and can provide diagnostics and therapeutics for compromised orphan foals such as plasma administration and health checks.</p>
      </div>
    </div>
    <div class="photo" role="img" aria-label="Chestnut horse with a white blaze and flowing mane running"
      style="left:0;right:0;bottom:0;height:300px;background:radial-gradient(ellipse at 60% 55%, #9a4a22 0%, #b9683a 35%, rgba(200,215,170,0) 75%);"></div>
  </article>

  <article class="panel panel--contact">
    <div class="photo" role="img" aria-label="Two horses looking over a wooden fence"
      style="left:0;right:0;top:0;height:92px;background:linear-gradient(180deg,#9cc3e4 0%,#c9b58e 55%,rgba(238,243,245,0) 100%);"></div>
    <div class="content contact" style="top:112px">
      <div class="brand-name"><span class="dot"></span>Willowmere</div>
      <p class="sub">Willowmere Vet Practice<br>including Nest2Nurse</p>
      <div class="contact-item">
        <svg width="12" height="12" viewBox="0 0 24 24"><path fill="#f26f21" d="M6.6 10.8a15 15 0 0 0 6.6 6.6l2.2-2.2a1 1 0 0 1 1-.25 11.4 11.4 0 0 0 3.6.57 1 1 0 0 1 1 1V20a1 1 0 0 1-1 1A17 17 0 0 1 3 4a1 1 0 0 1 1-1h3.5a1 1 0 0 1 1 1c0 1.25.2 2.45.57 3.57a1 1 0 0 1-.25 1z"/></svg>
        0491583620<br>0438261597
      </div>
      <div class="contact-item">
        <svg width="12" height="10" viewBox="0 0 24 18"><rect width="24" height="18" rx="2" fill="#f26f21"/><path d="M1 2l11 8 11-8" stroke="#fff" stroke-width="2" fill="none"/></svg>
        Your Email Goes Here
      </div>
      <div class="contact-item">
        <svg width="12" height="12" viewBox="0 0 24 24"><circle cx="12" cy="12" r="10" fill="none" stroke="#f26f21" stroke-width="2"/><ellipse cx="12" cy="12" rx="4" ry="10" fill="none" stroke="#f26f21" stroke-width="2"/><path d="M2 12h20" stroke="#f26f21" stroke-width="2"/></svg>
        Your Website Goes Here
      </div>
      <div class="contact-item">
        <svg width="12" height="12" viewBox="0 0 24 24"><circle cx="12" cy="12" r="10" fill="none" stroke="#f26f21" stroke-width="2.5"/><path d="M12 6v6l4 3" stroke="#f26f21" stroke-width="2.5" fill="none"/></svg>
        Your Hours Goes Here
      </div>
      <div class="contact-item">
        <svg width="11" height="14" viewBox="0 0 20 26"><path fill="#f26f21" d="M10 0a9 9 0 0 0-9 9c0 7 9 17 9 17s9-10 9-17a9 9 0 0 0-9-9zm0 12.5A3.5 3.5 0 1 1 10 5.5a3.5 3.5 0 0 1 0 7z"/></svg>
        218 Pellbrook Lane<br>Tarrick. Vic. 3872
      </div>
    </div>
  </article>

  <article class="panel panel--cover">
    <div class="photo" role="img" aria-label="Young woman standing with a mare and her foal in a paddock"
      style="left:0;right:0;top:40px;bottom:0;background:radial-gradient(ellipse at 45% 40%, #6b5f52 0%, #4a463f 40%, #2b2d2c 80%);"></div>
    <div class="cover-brand brand-name"><span class="dot"></span>Willowmere</div>
    <h1 class="headline">
      <span class="l1" style="display:block">Turn Your</span>
      <span class="l2" style="display:block">PASSION</span>
      <span class="l3" style="display:block">For Horses Into a Job</span>
    </h1>
  </article>
</section>

<section class="spread spread--inside" aria-label="Brochure inside">
  <article class="panel panel--mares">
    <div class="content" style="top:14px">
      <h2 class="tag">Mares</h2>
      <div class="body-text">
        <p>Nest2Nurse mares have been selected for mothering ability and temperament, and have all carried and raised at least one foal of their own. Many have already been successful foster mothers in one or more of the last five breeding seasons.</p>
        <p>The mares are not currently pregnant and are given a carefully designed course of hormones to induce lactation when required. The milk produced is not colostrum, but is completely normal and equivalent to that which they would have had if the foal was theirs by birth.</p>
        <p>There is published scientific information (in addition to our own experience and that of the owners of previous graduates of our programme) that growth and development of foals raised by induced lactation is identical to that of foals raised by their birth mothers.</p>
      </div>
      <h2 class="tag" style="margin-top:10px">Fostering</h2>
      <div class="body-text">
        <p>During the few days when the mare’s udder is developing, mare and foal are kept next separately but in close proximity, allowing bonding to begin and reducing stress on the orphan.</p>
        <p>The fostering is completed once the mare has enough milk to feed the foal, and our experienced handlers ensure that joining the two goes smoothly.</p>
        <p>Once they are together the mare completely accepts the foal as her own, and the foal can suckle freely – at this stage we continue to offer supplementary feeds until they are not needed.</p>
        <p>The mare and foal are then a normal unit and can return to the foal owner’s care until weaning – ensuring optimum nutrition and behaviour for the foal and excellent outcomes in performance, relationships with other horses, and interaction with humans.</p>
      </div>
    </div>
  </article>

  <article class="panel panel--safety">
    <div class="photo" role="img" aria-label="Three horses galloping across a field"
      style="left:0;right:0;top:0;height:120px;background:radial-gradient(ellipse at 50% 55%, #7a4a2c 0%, #a9825e 35%, rgba(207,227,243,0) 75%);"></div>
    <div class="content" style="top:138px">
      <h2 class="tag">Complete Safety</h2>
      <div class="body-text">
        <p>Mares recognise their birth foal by scent - a unique bond established during the first few minutes of the foal’s life - and only a small percentage of mares who have lost their own foal will readily accept a substitute.</p>
        <p>When a mare who has lost her birth foal is offered an orphan, it is very normal and common for her to respond with aggression - to the danger of the foal and the human handler.</p>
        <p>Nest2Nurse mares have no birth foal in the current season, and are happy to adopt any foal who is placed close to them during the hormone treatment period.</p>
        <p>This makes for total foal and handler safety.</p>
      </div>
    </div>
    <div class="photo" role="img" aria-label="Dark bay horse rearing beside a paddock fence"
      style="left:40%;right:-60%;bottom:0;height:260px;background:radial-gradient(ellipse at 50% 55%, #4a2a1c 0%, #6e5a45 35%, rgba(201,215,166,0) 75%);"></div>
  </article>

  <article class="panel panel--career">
    <div class="content" style="top:14px">
      <h2 class="tag">Career Mothers</h2>
      <div class="body-text">
        <p>Being dedicated career mothers with no other job in life, our mares are free to accompany their new foals home and stay with them as long as required. No foals are weaned and left without a mother in our programme, and our beautiful mares who would otherwise not be bred, are given a foal every year and a wonderful lifelong purpose.</p>
        <p>Every single orphan’s human family has admired and appreciated our beautiful mares, with many offering to give them a home for life. Each season as the orphans are weaned, we welcome our mares home to Willowmere to prepare for the next foal in need – a job they totally love! – just as if they were in a natural breeding situation.</p>
      </div>
      <h2 class="tag" style="margin-top:10px">Excellent Success Rate</h2>
      <div class="body-text">
        <p>After seven years of perfecting the fostering method, Nest2Nurse can claim total success: we have now documented almost 50 fosterings over the last five breeding seasons. We have never been entrusted with an orphan foal that we have not been able to provide with a beautiful foster mum.</p>
      </div>
    </div>
  </article>
</section>

</body>
</html>
```